Lawn Sign For Construction Projects - Vantor Power

This contest is for a lawn sign that will be placed in the front yard of recently completed construction projects. The goal here is to have a bold advertising sign that is visible from a vehicle driving past.

We are still deciding on the default size for our sign, we also may use multiple sizes. The two sizes we will more than likely be using are: 18"h x 24"w and 24"h x 36"w.

Preference will be given to designers that submit original designs that tie into our current brand and are either in both the size formats listed above or are easy to scale in photoshop or illustrator.

In the files, you will see our logo and an example of a lawn sign.

Please contact us with any questions or comments you may have!

Thank You,
- The Vantor Power Team

Industry/Entity Type

Residential Construction

Colors
34a7d8
ffffff
faa54b

Requirements
Nice to have
• 1. The sign must tie into our current branding and color scheme.
• 2. The sign must be clearly visible and readable.
• 3. The sign must include our phone number in readable print.
• 4. Our website written in small print along the bottom of the sign.
• 5. Must mention we install the following products:
• a.) Solar
• b.) Roofing
• c.) Windows
• d.) Artificial Lawn
• e.) Whole House Fans
• f.) Patio Covers

```html
<!DOCTYPE html>
<html lang="en">
<head>
<meta charset="utf-8">
<title>Vantor Power Lawn Sign</title>
<link rel="stylesheet" href="https://fonts.googleapis.com/css2?family=Open+Sans:wght@400;600;700&display=swap">
<style>
  :root {
    --band-black: #000000;
    --sun-orange: #f47b20;
    --mid-orange: #f89a1c;
    --sun-yellow: #fdc80e;
    --ink: #0a0a0a;
    --brand-blue: #1f7cc1;
    --brand-orange: #ef7a2b;
    --glow: #ffffff;
  }
  html, body {
    margin: 0;
    padding: 0;
    overflow: hidden;
    background: #ffffff;
  }
  .lawn-sign {
    position: relative;
    width: 1200px;
    height: 900px;
    overflow: hidden;
    font-family: "Open Sans", Arial, sans-serif;
    background: linear-gradient(180deg, var(--sun-orange) 24%, var(--mid-orange) 55%, var(--sun-yellow) 100%);
  }
  .sun-glow {
    position: absolute;
    inset: 216px 0 0 0;
    background:
      radial-gradient(ellipse 170px 90px at 600px 30px, rgba(255,255,255,0.95), rgba(255,255,255,0) 100%),
      radial-gradient(ellipse 520px 70px at 600px 20px, rgba(255,255,255,0.55), rgba(255,255,255,0) 100%),
      radial-gradient(ellipse 260px 320px at 690px 180px, rgba(255,240,200,0.35), rgba(255,255,255,0) 100%),
      radial-gradient(circle 120px at 190px 500px, rgba(255,230,120,0.25), rgba(255,255,255,0) 100%);
  }
  .brand-band {
    position: absolute;
    top: 0;
    left: 0;
    width: 1200px;
    height: 216px;
    background: var(--band-black);
  }
  .brand-mark {
    position: absolute;
    left: 558px;
    top: 40px;
    width: 84px;
    height: 84px;
  }
  .brand-name {
    position: absolute;
    top: 126px;
    left: 0;
    width: 1200px;
    text-align: center;
    font-size: 46px;
    line-height: 1;
    font-weight: 700;
    letter-spacing: -1px;
    color: var(--brand-blue);
    margin: 0;
  }
  .headline-lead, .headline-main, .phone, .website {
    position: absolute;
    margin: 0;
    line-height: 1;
    color: var(--ink);
    white-space: nowrap;
  }
  .headline-lead {
    left: 40px;
    top: 290px;
    font-size: 131px;
    font-weight: 400;
    letter-spacing: -3px;
  }
  .headline-main {
    left: 50px;
    top: 400px;
    font-size: 270px;
    font-weight: 700;
    letter-spacing: -6px;
  }
  .phone {
    left: 406px;
    top: 675px;
    font-size: 120px;
    font-weight: 400;
    letter-spacing: -1px;
  }
  .website {
    left: 416px;
    top: 826px;
    font-size: 38px;
    font-weight: 400;
  }
</style>
</head>
<body>
  <main class="lawn-sign">
    <div class="sun-glow" role="img" aria-label="Bright sun glow with soft rays and lens flare over an orange sky"></div>

    <header class="brand-band">
      <svg class="brand-mark" viewBox="0 0 84 84" aria-hidden="true">
        <circle cx="42" cy="42" r="38" fill="none" stroke="var(--brand-orange)" stroke-width="7"/>
      </svg>
      <p class="brand-name">VANTOR POWER</p>
    </header>

    <h1 class="headline-lead">We’ve Gone</h1>
    <p class="headline-main">SOLAR</p>
    <p class="phone">044-555-0192</p>
    <p class="website">www.vantorpower.com</p>
  </main>
</body>
</html>
```